ASL Learning Website Application Pages Redesign

Introduction:
We need a redesign of the internal pages of our website, SignQuiverly.com. The current website design has been in place for many years and is not mobile friendly. We want an updated design that makes the site look cleaner, more professional, and mobile accessible. We are looking for a design that eliminates the clutter on each page, and makes the site simple and easy to use. We will be interested in your design if it is unique and creative. Don't be afraid to completely change the look of the site.

We need the designs sliced up into clean HTML files that are responsive and work well on both mobile and desktop computers. We will implement the PHP needed to make the pages functional.

About Us:
SignQuiverly is a subscription-based website for American Sign Language (ASL) video lessons. The content is for anyone who wishes to learn ASL, regardless of age. It has been designed to instruct Deaf students, parents of Deaf children, and the community-at-large. All lessons are taught by Deaf experts of ASL.

Overview:
The website before log-in does not need any changes. There are five key pages within the internal website (after log-in) that need to be redesigned; they are listed below. Note that some pages (Dictionary and Activity) have multiple sub-pages, so there are about 6-8 pages in total to design, depending on how you decide to approach this (more info in the pages’ respective instruction documents).

The new page designs should retain their existing features, and as stated before, should be mobile friendly. However, you may combine, collapse, or completely change the look of these features. Each page to redesign has a separate instruction document attachment, and screenshots of the current version of the page. Our logo has also been attached. If you want to see the website pages for yourself, you can also go to our website (SignQuiverly.com) and use a free trial to get access to the internal site.

As for design preferences, we want our site to be modern-looking and mature. We’re looking for an inviting, educational style that can attract both high school students and adults. We’re happy with the current font and color scheme, but we’re always open to ideas!

Additional Notes:
- Every page has the same header and footer. You could keep these the same, or change them, based on your discretion.
- Currently, every page also has a breadcrumb. The breadcrumb is unnecessary and you may remove it. However, the “add/remove from favorites” button on the right of the breadcrumb is necessary to keep somewhere on the page.

Pages:
Here’s a list of the five key pages we need redesigned:
- Dashboard
- Dictionary
- Lesson
- Activity
- All Lessons

Each page has its own instruction document. These are attached separately.

Just purchased a $150 for Top designers. I need to give them time to submit their designs . Can I have 7 more days?

Target Market(s)

Deaf students, parents of Deaf children, and the community-at-large interested in learning ASL

Coding

Number of Pages Required

5+ page

Font styles to use
Sans Serif

Requirements
Must have
• Responsive design - the full application experience should be available on mobile devices.
Follow the directions on the design brief.
Nice to have
• Be creative! Please play around with, or even completely change, the look of the site.

```html
<!DOCTYPE html>
<html lang="en">
<head>
<meta charset="utf-8">
<title>SignQuiverly – Mobile View</title>
<link href="https://fonts.googleapis.com/css2?family=Montserrat:wght@600;700;800&family=Roboto:wght@400;500&display=swap" rel="stylesheet">
<style>
:root{
  --green:#00cc33;
  --orange:#f0a035;
  --ink:#111111;
  --muted:#777777;
  --paper:#ffffff;
  --screen:#f6f6f6;
  --line:#e6e6e6;
}
*{box-sizing:border-box;margin:0;padding:0}
html,body{width:1200px;height:1200px;overflow:hidden;background:var(--paper)}
body{font-family:"Roboto",Arial,sans-serif;color:var(--ink)}
.board{position:relative;width:1932px;height:1932px;transform:scale(.62112);transform-origin:0 0;overflow:hidden;background:var(--paper)}
.backdrop{position:absolute;inset:0}
.abs{position:absolute}
.brand-name{font-family:"Montserrat",Arial,sans-serif;font-weight:700;color:var(--ink);display:flex;align-items:center;gap:14px;white-space:nowrap}
.brand-name .mark{display:inline-block;background:var(--green)}
.hero-brand{left:235px;top:270px;font-size:58px}
.hero-brand .mark{width:40px;height:40px}
.title{left:60px;top:830px;width:656px;text-align:center;font-family:"Montserrat",Arial,sans-serif;font-weight:800;font-size:100px;line-height:118px}

/* phone screen */
.phone{left:732px;top:62px;width:400px;height:1900px;background:var(--screen);box-shadow:0 4px 30px rgba(0,0,0,.12)}
.status{height:43px;background:var(--paper);display:flex;justify-content:space-between;align-items:center;padding:0 28px 0 34px;font-size:14px;font-weight:500}
.status-icons{display:flex;gap:6px;align-items:center}
.appbar{height:67px;background:var(--paper);border-bottom:2px solid var(--line);display:flex;align-items:center;justify-content:space-between;padding:0 17px 0 18px}
.appbar .brand-name{font-size:20px;gap:6px}
.appbar .mark{width:10px;height:10px}
.avatar{width:40px;height:40px;border-radius:50%;background:linear-gradient(135deg,#c9b8a8,#8a7768)}
.welcome{padding:12px 18px 0}
.welcome h1{font-family:"Montserrat",Arial,sans-serif;font-weight:700;font-size:44px;line-height:52px}
.link{color:var(--orange);font-size:17px}
.welcome .link{display:block;margin-top:8px}
.fav-btn{display:inline-flex;align-items:center;gap:12px;margin-top:18px;height:47px;padding:0 16px 0 14px;border:2px solid var(--green);border-radius:6px;background:var(--paper);font-size:17px}
.card{position:absolute;left:18px;width:365px;background:var(--paper);border-radius:6px;box-shadow:0 2px 6px rgba(0,0,0,.1);overflow:hidden}
.card-head{background:var(--green);height:68px;padding:18px 20px;font-family:"Montserrat",Arial,sans-serif;font-weight:600;font-size:28px;line-height:32px}
.pages-grid{display:grid;grid-template-columns:repeat(3,1fr);padding:14px 0 0;row-gap:14px}
.page-item{text-align:center;font-size:13.5px;font-weight:500;line-height:16px;height:104px}
.page-item svg{display:block;margin:0 auto 8px}
.rec-block{text-align:center;padding:30px 0 0}
.rec-block .label{font-size:17px;font-weight:500}
.rec-block .value{color:var(--orange);font-size:21px;margin-top:18px;line-height:26px}
.rec-divider{height:2px;background:var(--line);margin:30px 14px 0}
.lessons-head{height:96px;padding:16px 18px}
.lessons-head .more{font-family:"Roboto",Arial,sans-serif;font-size:17px;font-weight:400;margin-top:6px;display:flex;align-items:center;gap:8px}
.lesson-grid{position:absolute;left:36px;top:1255px;width:330px;display:grid;grid-template-columns:154px 154px;column-gap:20px;row-gap:20px}
.lesson-card{height:212px;background:var(--paper);border-radius:6px;box-shadow:0 2px 6px rgba(0,0,0,.1);overflow:hidden}
.lesson-card .photo{height:115px}
.lesson-card h3{font-size:17px;font-weight:500;padding:18px 10px 0}
.lesson-card p{font-size:13px;color:var(--muted);padding:30px 10px 0;line-height:16px}

/* right panel */
.panel{left:1345px;top:0;width:400px;height:1855px;background:#fafafa;box-shadow:0 4px 30px rgba(0,0,0,.12)}
.topcards{position:absolute;left:17px;top:0;width:365px;height:105px;background:var(--paper);border-radius:0 0 6px 6px;box-shadow:0 2px 6px rgba(0,0,0,.1);overflow:hidden}
.mini{position:absolute;top:-20px;width:155px;height:95px;background:var(--paper);border-radius:6px;box-shadow:0 2px 6px rgba(0,0,0,.12);padding:0 10px}
.mini h3{font-size:17px;font-weight:500;margin-top:6px;height:20px}
.mini p{font-size:13px;color:var(--muted);line-height:16px;margin-top:30px}
.progress{top:125px;left:17px;height:943px}
.progress .card-head{display:flex;justify-content:space-between;align-items:center;padding:0 18px 0 20px}
.kebab{display:flex;flex-direction:column;gap:4px}
.kebab i{width:5px;height:5px;border-radius:50%;background:var(--ink);display:block}
.entry{margin:0 20px 0 24px;height:175px;padding-top:20px;border-bottom:2px solid var(--line)}
.entry:last-child{border-bottom:none}
.entry .date{font-size:14px}
.entry .row{display:flex;justify-content:space-between;font-size:17px;margin-top:10px}
.entry .meta{display:flex;font-size:17px;margin-top:9px;align-items:baseline}
.entry .meta span{font-size:13.5px;color:var(--muted);width:74px}
.entry .link{display:block;margin-top:9px}
.footer{position:absolute;left:0;top:1086px;width:400px;border-top:3px solid var(--green);padding:0 17px}
.footer .brand-name{justify-content:center;font-size:44px;margin-top:62px;gap:12px}
.footer .mark{width:28px;height:28px}
.footer h4{font-family:"Montserrat",Arial,sans-serif;font-weight:600;font-size:23px;margin-top:52px}
.quick{display:grid;grid-template-columns:145px 200px;font-size:17px;row-gap:19px;margin:16px 0 0 4px}
.contact{margin-top:20px;padding-left:4px}
.contact li{list-style:none;display:flex;align-items:center;gap:14px;font-size:17px;margin-bottom:18px}
.footer-rule{height:2px;background:var(--green);margin-top:26px}
.socials{display:flex;justify-content:center;gap:22px;margin-top:22px}
.socials i{width:48px;height:48px;border-radius:50%;border:2px solid var(--green);display:block}
.copy{text-align:center;font-size:16.5px;line-height:20px;margin-top:30px}
</style>
</head>
<body>
<div class="board">
  <svg class="backdrop" width="1932" height="1932" viewBox="0 0 1932 1932" aria-hidden="true">
    <g fill="none" stroke="#00cc33" stroke-width="26">
      <polyline points="-20,245 388,640 760,282"/>
      <polyline points="-20,1702 366,1308 760,1702"/>
      <polyline points="970,-5 1012,20 962,68"/>
      <line x1="1740" y1="1372" x2="1950" y2="1165"/>
      <line x1="1740" y1="1590" x2="1950" y2="1790"/>
    </g>
    <polygon fill="#00cc33" points="0,1932 0,1858 366,1475 740,1858 740,1932"/>
    <polygon fill="#00cc33" points="1745,0 1932,0 1932,425 1745,240"/>
  </svg>

  <div class="abs brand-name hero-brand"><span class="mark"></span>SignQuiverly</div>
  <div class="abs title">Mobile<br>View</div>

  <section class="abs phone">
    <div class="status">
      <span>9:41</span>
      <span class="status-icons">
        <svg width="18" height="11" viewBox="0 0 18 11"><rect x="0" y="7" width="3" height="4" fill="#111"/><rect x="5" y="5" width="3" height="6" fill="#111"/><rect x="10" y="2" width="3" height="9" fill="#111"/><rect x="15" y="0" width="3" height="11" fill="#111"/></svg>
        <svg width="16" height="12" viewBox="0 0 16 12"><path d="M1 4a10 10 0 0 1 14 0M3.5 6.5a6.5 6.5 0 0 1 9 0M6 9a3 3 0 0 1 4 0" stroke="#111" stroke-width="1.8" fill="none"/><circle cx="8" cy="11" r="1" fill="#111"/></svg>
        <svg width="22" height="11" viewBox="0 0 22 11"><rect x="0" y="1" width="20" height="9" rx="2" fill="#111"/><rect x="20.5" y="4" width="1.5" height="3" fill="#111"/></svg>
      </span>
    </div>
    <header class="appbar">
      <svg width="20" height="20" viewBox="0 0 20 20"><path d="M0 3h20M0 10h20M0 17h20" stroke="#111" stroke-width="2"/></svg>
      <div class="brand-name"><span class="mark"></span>SignQuiverly</div>
      <div class="avatar" role="img" aria-label="User profile photo"></div>
    </header>
    <div class="welcome">
      <h1>Welcome<br>Marenwick</h1>
      <span class="link">Show Welcome Message &nbsp;›</span>
      <button class="fav-btn"><svg width="22" height="22" viewBox="0 0 22 22"><rect x="1" y="1" width="20" height="20" fill="none" stroke="#111" stroke-width="1.6"/><path d="M11 5v12M5 11h12" stroke="#111" stroke-width="1.6"/></svg>Add to Favorites</button>
    </div>

    <div class="card" style="top:343px;height:405px">
      <div class="card-head">My Pages</div>
      <div class="pages-grid">
        <div class="page-item"><svg width="66" height="52" viewBox="0 0 66 52" fill="none" stroke="#f0a035" stroke-width="3"><path d="M33 8C25 3 12 3 4 6v42c8-3 21-3 29 2 8-5 21-5 29-2V6c-8-3-21-3-29 2zM33 8v42"/><path d="M9 10v32M57 10v32"/></svg>Dictionary</div>
        <div class="page-item"><svg width="50" height="52" viewBox="0 0 50 52" fill="none" stroke="#f0a035" stroke-width="3"><path d="M2 2h46v12h-5l-2-6H30v38h7v4H13v-4h7V8H9l-2 6H2z"/></svg>My Vocabulary</div>
        <div class="page-item"><svg width="44" height="52" viewBox="0 0 44 52" fill="none" stroke="#f0a035" stroke-width="3"><path d="M8 2h30v36L26 50H8z"/><path d="M2 10v40h24M16 14h16M16 22h16M16 30h10"/></svg>Favorites</div>
        <div class="page-item"><svg width="52" height="52" viewBox="0 0 52 52" fill="none" stroke="#f0a035" stroke-width="3"><circle cx="26" cy="26" r="23"/><path d="M27 22l-4 16M24 38h6" /><circle cx="28" cy="15" r="2" fill="#f0a035"/></svg>Tips and<br>Grammar</div>
        <div class="page-item"><svg width="52" height="52" viewBox="0 0 52 52" fill="none" stroke="#f0a035" stroke-width="3"><rect x="19" y="2" width="14" height="10"/><path d="M26 12v12M8 24h36M8 24v14M26 24v14M44 24v14"/><rect x="2" y="38" width="12" height="12"/><rect x="20" y="38" width="12" height="12"/><rect x="38" y="38" width="12" height="12"/></svg>Multiple<br>Meanings</div>
        <div class="page-item"><svg width="52" height="52" viewBox="0 0 52 52" fill="none" stroke="#f0a035" stroke-width="3"><rect x="12" y="10" width="38" height="40"/><path d="M6 4h38v6M6 4v40h6M20 22h22M20 30h22M20 38h22"/></svg>Lesson List</div>
        <div class="page-item"><svg width="52" height="52" viewBox="0 0 52 52"><circle cx="26" cy="26" r="23" fill="none" stroke="#f0a035" stroke-width="3"/><path d="M26 13l4 9 9 1-7 6 2 9-8-5-8 5 2-9-7-6 9-1z" fill="#f0a035"/></svg>My Lessons</div>
      </div>
    </div>

    <div class="card" style="top:768px;height:348px">
      <div class="card-head">Recommended</div>
      <div class="rec-block"><div class="label">Next Lesson</div><div class="value">Colors</div></div>
      <div class="rec-divider"></div>
      <div class="rec-block"><div class="label">Next Activity</div><div class="value">Choose the<br>Correct Sentence</div></div>
    </div>

    <div class="card" style="top:1136px;height:96px;border-radius:6px 6px 0 0">
      <div class="card-head lessons-head">Lessons
        <div class="more">More Lessons <svg width="10" height="18" viewBox="0 0 10 18"><path d="M1 1l8 8-8 8" stroke="#111" stroke-width="2" fill="none"/></svg></div>
      </div>
    </div>

    <div class="lesson-grid">
      <article class="lesson-card"><div class="photo" role="img" aria-label="Streaks of rainbow paint colors" style="background:linear-gradient(90deg,#f0a020,#e0302a,#30a040,#2050c0,#8040a0)"></div><h3>Colors</h3><p>Beginner</p></article>
      <article class="lesson-card"><div class="photo" role="img" aria-label="Person sitting by a campfire on a beach" style="background:linear-gradient(180deg,#b9b6b0,#5a5048 70%,#d08030)"></div><h3>Survival Words</h3><p>Beginner</p></article>
      <article class="lesson-card"><div class="photo" role="img" aria-label="Question mark drawn on a tan wall" style="background:linear-gradient(135deg,#d3b28e,#b89270)"></div><h3>Deaf Culture 1</h3><p>Beginner,<br>Deaf Culture</p></article>
      <article class="lesson-card"><div class="photo" role="img" aria-label="Hand forming a fingerspelled letter" style="background:linear-gradient(135deg,#f4f4f4,#e2d0c4)"></div><h3>Fingerspelling 1</h3><p>Beginner,<br>Fingerspelling</p></article>
      <article class="lesson-card"><div class="photo" role="img" aria-label="Parent and child reading together at home" style="background:linear-gradient(135deg,#e8e4de,#9a7058)"></div><h3>Family</h3></article>
      <article class="lesson-card"><div class="photo" role="img" aria-label="The word want written on a dark surface" style="background:linear-gradient(135deg,#3a3026,#6a5e48)"></div><h3>Pronouns</h3></article>
    </div>
  </section>

  <section class="abs panel">
    <div class="topcards">
      <div class="mini" style="left:18px"><h3>Family</h3><p>Beginner</p></div>
      <div class="mini" style="left:191px"><h3>Pronouns</h3><p>Beginner,<br>Deaf Culture</p></div>
    </div>

    <div class="card progress">
      <div class="card-head">Your Progress <span class="kebab"><i></i><i></i><i></i></span></div>
      <div class="entry"><div class="date">05/25/2021</div><div class="row"><span>Colors</span><span>100 %</span></div><div class="meta"><span>Activity &nbsp;:</span>Match the vocabulary</div><div class="meta"><span>Attemps :</span>1</div><span class="link">Review Lesson, Retry Activity</span></div>
      <div class="entry"><div class="date">05/25/2021</div><div class="row"><span>Numbers 1-20</span><span>100 %</span></div><div class="meta"><span>Activity &nbsp;:</span>Grammar instruction</div><div class="meta"><span>Attemps :</span>1</div><span class="link">Review Lesson, Retry Activity</span></div>
      <div class="entry"><div class="date">05/25/2021</div><div class="row"><span>Numbers 1-20</span><span>100 %</span></div><div class="meta"><span>Activity &nbsp;:</span>Do these video match?</div><div class="meta"><span>Attemps :</span>1</div><span class="link">Review Lesson, Retry Activity</span></div>
      <div class="entry"><div class="date">05/25/2021</div><div class="row"><span>Meet &amp; Greet</span><span>80 %</span></div><div class="meta"><span>Activity &nbsp;:</span>Choose the correct location</div><div class="meta"><span>Attemps :</span>1</div><span class="link">Review Lesson, Retry Activity</span></div>
      <div class="entry"><div class="date">05/25/2021</div><div class="row"><span>Meet &amp; Greet</span><span>100 %</span></div><div class="meta"><span>Activity &nbsp;:</span>English to ASL Practice</div><div class="meta"><span>Attemps :</span>1</div><span class="link">Review Lesson, Retry Activity</span></div>
    </div>

    <footer class="footer">
      <div class="brand-name"><span class="mark"></span>SignQuiverly</div>
      <h4>Quick Links</h4>
      <div class="quick">
        <span>Home</span><span>Group Rate Form</span>
        <span>Try it Free</span><span>Teacher Guide</span>
        <span>Contact Us</span><span>Gift Certificates</span>
        <span>About Us</span><span>FAQs</span>
        <span></span><span>Privacy Policy</span>
      </div>
      <h4 style="margin-left:5px;margin-top:44px">Contact Us</h4>
      <ul class="contact">
        <li><svg width="22" height="20" viewBox="0 0 22 20"><rect x="1" y="1" width="20" height="18" fill="#111"/><path d="M3 4l8 6 8-6" stroke="#fff" stroke-width="1.6" fill="none"/></svg>PO Box 50872, Brookfield Vale, MI 48090</li>
        <li><svg width="22" height="20" viewBox="0 0 22 20"><path d="M4 1l4 1 1 5-3 2c1 3 3 5 6 6l2-3 5 1 1 4c-1 2-3 3-5 2C8 17 4 12 3 6 2 4 3 2 4 1z" fill="#111"/></svg>(555) 014-2738</li>
        <li><svg width="22" height="20" viewBox="0 0 22 20"><rect x="1" y="4" width="20" height="14" fill="none" stroke="#111" stroke-width="1.8"/><path d="M1 4l10 8 10-8" stroke="#111" stroke-width="1.8" fill="none"/></svg>info@signquiverly.com</li>
      </ul>
      <div class="footer-rule"></div>
      <div class="socials"><i></i><i></i><i></i><i></i><i></i></div>
      <p class="copy">Copyrights © 2021, SignQuiverly.<br>All rights reserved. Terms &amp; Conditions</p>
    </footer>
  </section>
</div>
</body>
</html>
```